Larchmont Vale Rehab and Wellness Postcard

This is a postcard for our chiropractic office, to raise awareness of our practice. Please refer to our grand opening flyer for contact information and logo. Please include the following:
Larchmont Vale Rehab and Wellness
Chiropractic & Wellness
Spinal Correction
Injury Rehabilitation
Tired of living with Fatigue, Allergies, High/Low Blood Pressure, Headaches, Numbness/Tingling in Hands/Feet, Frequent Infection, Back Pain, Neck Pain or ANY Other Health Problems?
Call Today for a Free Consultation with the Doctor!
(Space is Limited, Please Call to Reserve)

```html
<!DOCTYPE html>
<html lang="en">
<head>
<meta charset="utf-8">
<title>Larchmont Vale Rehab and Wellness Postcard</title>
<link href="https://fonts.googleapis.com/css2?family=Roboto:wght@400;500;700&family=Roboto+Condensed:ital,wght@0,400;0,500;0,700;1,700&display=swap" rel="stylesheet">
<style>
  :root {
    --page: #ffffff;
    --card: #ffffff;
    --card-edge: #d9e2ec;
    --band: #6e99c9;
    --accent: #6f9ac8;
    --brand: #4a7fc0;
    --headline-blue: #2f74c0;
    --ink: #14181f;
    --sky-top: #6b9fd6;
    --sky-mid: #a9c9ea;
    --sky-low: #e3eef8;
    --spine-pale: #c9dcee;
  }
  * { box-sizing: border-box; margin: 0; padding: 0; }
  html, body {
    width: 892px; height: 1200px; overflow: hidden;
    background: var(--page);
    font-family: "Roboto", Arial, sans-serif;
  }
  .sheet { position: relative; width: 892px; height: 1200px; }
  .card {
    position: absolute; left: 12px; width: 868px; height: 580px;
    background: var(--card); border: 1px solid var(--card-edge); overflow: hidden;
  }
  .card--front { top: 10px; }
  .card--back { top: 606px; }

  /* Front */
  .hero {
    position: absolute; left: 0; top: 0; width: 100%; height: 305px;
    background:
      radial-gradient(ellipse 160px 300px at 790px 170px, rgba(232,169,85,.55), rgba(90,120,190,.45) 45%, transparent 75%),
      radial-gradient(ellipse 300px 120px at 300px 120px, rgba(255,255,255,.7), transparent 70%),
      linear-gradient(180deg, var(--sky-top) 0%, var(--sky-mid) 55%, var(--sky-low) 100%);
  }
  .services-band {
    position: absolute; left: 0; top: 305px; width: 100%; height: 48px;
    background: var(--band); color: #fff;
    display: flex; align-items: center; justify-content: center; gap: 16px;
    font-weight: 700; font-size: 22px; letter-spacing: -.2px;
  }
  .services-band .dot { font-size: 16px; }
  .brand-name {
    position: absolute; color: var(--brand); font-weight: 500;
    display: flex; align-items: center; gap: 14px; line-height: 1.15;
  }
  .brand-name .mark { width: 22px; height: 22px; border-radius: 50%; background: var(--brand); flex: none; }
  .card--front .brand-name { left: 80px; top: 420px; font-size: 34px; width: 340px; }
  .front-address {
    position: absolute; left: 387px; top: 370px;
    color: var(--accent); font-weight: 700; font-size: 16px; letter-spacing: -.1px;
  }
  .contact-line {
    position: absolute; display: flex; align-items: center;
    color: var(--accent); font-weight: 700; white-space: nowrap;
  }
  .contact-line svg { flex: none; }
  .card--front .phone { left: 540px; top: 450px; font-size: 27px; gap: 14px; }
  .card--front .web { left: 538px; top: 505px; font-size: 21px; gap: 14px; }

  /* Back */
  .ailments {
    position: absolute; left: 54px; top: 56px; width: 336px;
    font-family: "Roboto Condensed", Arial, sans-serif; font-weight: 700;
    font-size: 19.5px; line-height: 27.5px; color: var(--headline-blue);
    white-space: nowrap; letter-spacing: -.2px;
  }
  .ailments .dark { color: var(--ink); }
  .ailments em { font-style: italic; color: var(--ink); }
  .consult-badge { position: absolute; left: 130px; top: 212px; }
  .consult-badge .badge-box {
    position: relative; width: 157px; height: 62px; background: var(--accent);
    color: #fff; font-family: "Roboto Condensed", Arial, sans-serif;
    padding: 7px 0 0 6px; line-height: 1;
  }
  .consult-badge .small { font-size: 13px; display: block; }
  .consult-badge .big { font-size: 21px; font-weight: 500; display: block; margin: 1px 0; }
  .consult-badge svg.phone-icon { position: absolute; right: 8px; top: 8px; }
  .consult-badge .tail { display: block; }
  .call-note {
    position: absolute; left: 54px; top: 308px; width: 336px;
    font-family: "Roboto Condensed", Arial, sans-serif; text-align: center;
    color: var(--ink); font-size: 15px; line-height: 19px;
  }
  .call-note strong { font-weight: 700; color: var(--headline-blue); }
  .card--back .brand-name { left: 92px; top: 366px; font-size: 24px; width: 260px; }
  .card--back .phone { left: 124px; top: 472px; font-size: 22px; gap: 10px; }
  .card--back .web { left: 124px; top: 510px; font-size: 17px; gap: 10px; }
  .spine-art {
    position: absolute; left: 402px; top: 48px; width: 64px; height: 500px;
    border-radius: 32px 20px 20px 32px;
    background: linear-gradient(180deg, var(--spine-pale), #a9c5e0 50%, var(--spine-pale));
  }
  .back-address {
    position: absolute; left: 480px; top: 56px; font-style: normal;
    font-family: "Roboto Condensed", Arial, sans-serif; font-weight: 500;
    font-size: 17px; line-height: 21.5px; color: var(--ink);
  }
</style>
</head>
<body>
<main class="sheet">

  <section class="card card--front">
    <div class="hero" role="img" aria-label="Bright blue sky with clouds and a translucent figure showing a glowing spine"></div>
    <div class="services-band">
      <span>Chiropractic &amp; Wellness</span><span class="dot">•</span>
      <span>Spinal Correction</span><span class="dot">•</span>
      <span>Injury Rehabilitation</span>
    </div>
    <div class="brand-name"><span class="mark"></span><span>Larchmont Vale Rehab</span></div>
    <p class="front-address">418 Orchard Avenue, Suite 210, Larchmont Vale, NJ 07991</p>
    <p class="contact-line phone">
      <svg width="18" height="26" viewBox="0 0 18 26"><rect x="1.5" y="1.5" width="15" height="23" rx="2" fill="none" stroke="#1e2630" stroke-width="2.4"/><line x1="2" y1="20" x2="16" y2="20" stroke="#1e2630" stroke-width="2"/></svg>
      <span>555-014-7720</span>
    </p>
    <p class="contact-line web">
      <svg width="24" height="24" viewBox="0 0 24 24" fill="none" stroke="#1e2630" stroke-width="1.8"><circle cx="12" cy="12" r="10"/><ellipse cx="12" cy="12" rx="4.5" ry="10"/><line x1="2" y1="12" x2="22" y2="12"/><path d="M4 6.5h16M4 17.5h16"/></svg>
      <span>larchmontvalerehab.com</span>
    </p>
  </section>

  <section class="card card--back">
    <p class="ailments">
      <em>TIRED</em> <span class="dark">of living with</span> Fatigue, Allergies,<br>
      High/Low Blood Pressure, Headaches,<br>
      Numbness/Tingling in Hands/Feet,<br>
      Frequent Infection, Back Pain, Neck<br>
      Pain <span class="dark">or</span> <em>ANY</em> <span class="dark">Other Health Problems?</span>
    </p>
    <div class="consult-badge">
      <div class="badge-box">
        <span class="small">SCHEDULE A</span>
        <span class="big">FREE</span>
        <span class="small">CONSULTATION</span>
        <svg class="phone-icon" width="40" height="46" viewBox="0 0 40 46" fill="none" stroke="#fff" stroke-width="2.4"><rect x="18" y="3" width="18" height="38" rx="3" transform="rotate(12 27 22)"/><path d="M6 30a8 8 0 0 1 6-10M2 31a13 13 0 0 1 9-15"/></svg>
      </div>
      <svg class="tail" width="64" height="28" viewBox="0 0 64 28"><path d="M0 0H64L60 28Z" fill="var(--accent)"/></svg>
    </div>
    <p class="call-note">
      <strong>Call Today for a Free Consultation with the Doctor!</strong><br>
      (Space is Limited, Please Call to Reserve)
    </p>
    <div class="brand-name"><span class="mark"></span><span>Larchmont Vale Rehab</span></div>
    <p class="contact-line phone">
      <svg width="15" height="22" viewBox="0 0 15 22"><rect x="1.2" y="1.2" width="12.6" height="19.6" rx="1.8" fill="none" stroke="#1e2630" stroke-width="2"/><line x1="1.5" y1="17" x2="13.5" y2="17" stroke="#1e2630" stroke-width="1.7"/></svg>
      <span>555-014-7720</span>
    </p>
    <p class="contact-line web">
      <svg width="20" height="20" viewBox="0 0 24 24" fill="none" stroke="#1e2630" stroke-width="1.9"><circle cx="12" cy="12" r="10"/><ellipse cx="12" cy="12" rx="4.5" ry="10"/><line x1="2" y1="12" x2="22" y2="12"/><path d="M4 6.5h16M4 17.5h16"/></svg>
      <span>larchmontvalerehab.com</span>
    </p>
    <div class="spine-art" role="img" aria-label="Pale blue illustration of a human spine in side view"></div>
    <address class="back-address">
      418 Orchard Avenue<br>Suite 210<br>Larchmont Vale, NJ 07991
    </address>
  </section>

</main>
</body>
</html>
```